Email Notification & Marketing Templates

I want to start with something like a newsletter or informational email, but i need Top Tips to Detect Phishing Scams. Something that i can send to users so they can follow it when receiving or exchanging emails. I will also need promotional items for my company that i can send to customers as well. It can be based on on our website QRVLINK.COM

Will also need:
newsletters
announcements
marketing emails
alerts
security notifications

Examples:Items such as Security Awareness Poster Series
Phishing Awareness
Password Security
Email Attachments
QR Code scams
Public WiFi safety

```html
<!DOCTYPE html>
<html lang="en">
<head>
<meta charset="UTF-8">
<title>Strengthen Your Passwords Today</title>
<link rel="stylesheet" href="https://fonts.googleapis.com/css2?family=Open+Sans:wght@400;600;700&family=Roboto:wght@500;700&display=swap">
<style>
  :root {
    --page-bg: #f3f6f7;
    --card-bg: #ffffff;
    --brand-green: #3f9a2c;
    --button-top: #5cbf2a;
    --button-bottom: #2f8a18;
    --ink: #1d1d1f;
    --ink-soft: #333a40;
    --rule-blue: #2a6c8e;
    --panel-bg: #eff2f4;
    --panel-line: #d6dbe0;
    --weak-bg: #fbe1e0;
    --weak-line: #f0b3b0;
    --weak-red: #d9363e;
    --strong-bg: #e6f5df;
    --strong-line: #b6dea3;
    --strong-green: #4caf3a;
    --icon-blue: #2b6d93;
    --hero-deep: #1d4f8c;
    --hero-mid: #2c8fb0;
  }
  * { box-sizing: border-box; margin: 0; padding: 0; }
  html, body { width: 1200px; height: 1200px; overflow: hidden; }
  body {
    background: var(--page-bg);
    font-family: "Open Sans", Arial, sans-serif;
    color: var(--ink);
  }
  .email {
    position: absolute;
    left: 214px; top: 0;
    width: 772px; height: 1200px;
    background: var(--card-bg);
  }
  .brand {
    position: absolute;
    left: 40px; top: 34px;
    display: flex; align-items: center; gap: 12px;
  }
  .brand-mark {
    width: 30px; height: 30px;
    background: var(--brand-green);
  }
  .brand-name {
    font-weight: 700;
    font-size: 26px;
    color: var(--brand-green);
    letter-spacing: 0.5px;
  }
  .hero {
    position: absolute;
    left: 0; top: 125px;
    width: 772px; height: 300px;
    border-top: 2px solid var(--rule-blue);
    border-bottom: 2px solid var(--rule-blue);
    background: linear-gradient(90deg, #ffffff 0%, #f4f8fb 32%, #cfe3ee 48%, var(--hero-mid) 70%, var(--hero-deep) 100%);
    overflow: hidden;
  }
  .hero-title {
    position: absolute;
    left: 40px; top: 92px;
    font-family: "Roboto", Arial, sans-serif;
    font-weight: 700;
    font-size: 43px;
    line-height: 1.08;
    color: var(--brand-green);
  }
  .hero-art {
    position: absolute;
    right: 0; top: 0;
    width: 400px; height: 100%;
    background: radial-gradient(ellipse at 55% 45%, rgba(99, 211, 200, 0.55) 0%, rgba(44, 143, 176, 0.3) 45%, rgba(29, 79, 140, 0) 75%);
  }
  .section-title {
    position: absolute;
    left: 0; width: 100%;
    text-align: center;
    font-weight: 600;
    color: var(--ink);
  }
  .why-title { top: 462px; font-size: 30px; }
  .why-sub { top: 516px; font-size: 24px; font-weight: 400; }
  .compare {
    position: absolute;
    top: 570px;
    width: 333px; height: 181px;
    background: var(--panel-bg);
    border: 1px solid var(--panel-line);
    border-radius: 8px;
    text-align: center;
  }
  .compare--weak { left: 40px; }
  .compare--strong { left: 399px; }
  .compare-label {
    margin-top: 20px;
    font-weight: 700;
    font-size: 21px;
    letter-spacing: 0.3px;
  }
  .sample-row {
    margin-top: 12px;
    display: flex; justify-content: center; align-items: center; gap: 8px;
    font-size: 20px;
  }
  .sample {
    padding: 2px 9px;
    border-radius: 6px;
    font-size: 20px;
  }
  .sample--weak { background: var(--weak-bg); border: 1px solid var(--weak-line); }
  .sample--strong { background: var(--strong-bg); border: 1px solid var(--strong-line); }
  .verdict { margin-top: 10px; display: block; margin-left: auto; margin-right: auto; }
  .compare-note { margin-top: 6px; font-size: 18px; color: var(--ink-soft); }
  .tips-title { top: 788px; font-size: 28px; }
  .tips {
    position: absolute;
    left: 58px; top: 836px;
    list-style: none;
  }
  .tip {
    display: flex; align-items: center;
    height: 57px;
    font-size: 21px;
    color: var(--ink-soft);
  }
  .tip-icon { width: 44px; height: 44px; margin-right: 22px; flex-shrink: 0; }
  .tip strong { color: var(--ink); font-weight: 700; margin-right: 6px; }
  .cta {
    position: absolute;
    left: 40px; top: 1039px;
    width: 692px; height: 71px;
    border-radius: 36px;
    background: linear-gradient(180deg, var(--button-top) 0%, var(--button-bottom) 100%);
    color: #ffffff;
    font-weight: 600;
    font-size: 29px;
    display: flex; align-items: center; justify-content: center;
    text-decoration: none;
  }
  .footer-rule {
    position: absolute;
    left: 40px; top: 1145px;
    width: 692px; height: 2px;
    background: var(--rule-blue);
  }
  .footer {
    position: absolute;
    left: 0; top: 1163px; width: 100%;
    text-align: center;
    font-size: 15px;
    color: var(--ink);
  }
  .footer a { color: var(--rule-blue); }
</style>
</head>
<body>
  <div class="email">
    <header class="brand">
      <span class="brand-mark"></span>
      <span class="brand-name">CNG Clearpath Network Group</span>
    </header>

    <section class="hero">
      <h1 class="hero-title">Strengthen Your<br>Passwords Today</h1>
      <div class="hero-art" role="img" aria-label="Illustration of a green padlock over a glowing circuit board with a password field"></div>
    </section>

    <h2 class="section-title why-title">Why It Matters</h2>
    <p class="section-title why-sub">Weak Passwords vs. Strong Passwords</p>

    <div class="compare compare--weak">
      <p class="compare-label">WEAK PASSWORDS</p>
      <div class="sample-row">
        <span class="sample sample--weak">123456</span> or <span class="sample sample--weak">password</span>
      </div>
      <svg class="verdict" width="26" height="26" viewBox="0 0 26 26" aria-hidden="true">
        <circle cx="13" cy="13" r="12" fill="var(--weak-red)"/>
        <path d="M8.5 8.5 L17.5 17.5 M17.5 8.5 L8.5 17.5" stroke="#fff" stroke-width="2.6" stroke-linecap="round"/>
      </svg>
      <p class="compare-note">Easy to guess, common, insecure.</p>
    </div>

    <div class="compare compare--strong">
      <p class="compare-label">STRONG PASSWORDS</p>
      <div class="sample-row">
        <span class="sample sample--strong">Bl9e#Riv3r!P@ss2024</span>
      </div>
      <svg class="verdict" width="26" height="26" viewBox="0 0 26 26" aria-hidden="true">
        <circle cx="13" cy="13" r="12" fill="var(--strong-green)"/>
        <path d="M7.5 13.5 L11.5 17.5 L18.5 9.5" fill="none" stroke="#fff" stroke-width="2.6" stroke-linecap="round" stroke-linejoin="round"/>
      </svg>
      <p class="compare-note">Long, unique, complex, secure.</p>
    </div>

    <h2 class="section-title tips-title">Tips for Stronger Passwords</h2>
    <ul class="tips">
      <li class="tip">
        <svg class="tip-icon" viewBox="0 0 44 44" aria-hidden="true">
          <g fill="none" stroke="var(--icon-blue)" stroke-width="2" stroke-linejoin="round">
            <rect x="4" y="16" width="36" height="12" rx="2" transform="rotate(-45 22 22)"/>
            <path d="M14 23 l3 3 M18 19 l3 3 M22 15 l3 3 M26 11 l3 3" stroke-linecap="round"/>
          </g>
        </svg>
        <span><strong>Long &amp; Unique:</strong>At least 12 characters, different for each site.</span>
      </li>
      <li class="tip">
        <svg class="tip-icon" viewBox="0 0 44 44" aria-hidden="true">
          <g fill="none" stroke="var(--icon-blue)" stroke-width="2">
            <rect x="4" y="14" width="36" height="22" rx="3"/>
            <path d="M20 14 v-5 h6 v-4" stroke-linecap="round"/>
            <path d="M9 20h3 M15 20h3 M21 20h3 M27 20h3 M33 20h2 M9 25h3 M15 25h3 M21 25h3 M27 25h3 M33 25h2 M13 30h18" stroke-linecap="round"/>
          </g>
        </svg>
        <span><strong>Mix it Up:</strong>Use uppercase, lowercase, numbers, and symbols.</span>
      </li>
      <li class="tip">
        <svg class="tip-icon" viewBox="0 0 44 44" aria-hidden="true">
          <g fill="none" stroke="var(--icon-blue)" stroke-width="2" stroke-linecap="round" stroke-linejoin="round">
            <path d="M22 4 L37 10 V21 C37 30 30 37 22 40 C14 37 7 30 7 21 V10 Z"/>
            <path d="M15 18 h13 l-3 -3 M29 25 h-13 l3 3"/>
          </g>
        </svg>
        <span><strong>Enable 2FA:</strong>Add an extra layer of protection.</span>
      </li>
    </ul>

    <a class="cta" href="#">Secure Your Account</a>

    <div class="footer-rule"></div>
    <p class="footer">© 2024 CNG Clearpath Network Group. All rights reserved. | <a href="#">Unsubscribe</a></p>
  </div>
</body>
</html>
```